Modern Brochure on A4 size - Tessaly Crane Int'l

- We are a educational company that takes children overseas to teach them English and experience new cultures. For this project we will be taking children from South Korea to the Washington D.C. area.
- I would like to have a brochure made using A4 size paper in a landscape view
- I have the logo already designed and can upload the correct file upon request.
- I have uploaded a layout format that I would like, but need help making a template that is modern and appealing to the eye.
- I would like picture on each page that are related to the topic and areas where I can insert information.
THANK YOU VERY MUCH!

Industry/Entity Type

Education

Font styles to use
Sans Serif

Colors
ffc214
f78f20
0456a4
3277b5

Requirements
Must have
• The logo on the cover. Please let me know if you need another type of file for the logo. I have several and wasn't sure what would be the best.
Nice to have
• https://kr.pinboardia.example/velotcraft2019/brochures/
• Here is a link to the styles that I prefer

```html
<!DOCTYPE html>
<html lang="en">
<head>
<meta charset="utf-8">
<title>Tessaly Crane Int'l – Brochure</title>
<link rel="stylesheet" href="https://fonts.googleapis.com/css2?family=Open+Sans:wght@300;400;600&display=swap">
<style>
  :root {
    --bg: #e6e6e6;
    --paper: #f7f7f7;
    --brand-blue: #0456a4;
    --mid-blue: #3277b5;
    --sky-blue: #3fa9e0;
    --sun-yellow: #ffc214;
    --sun-orange: #f78f20;
    --white: #ffffff;
  }
  * { box-sizing: border-box; margin: 0; padding: 0; }
  html, body {
    width: 1200px; height: 900px; overflow: hidden;
    background: var(--bg);
    font-family: "Open Sans", Arial, sans-serif;
  }
  .spread {
    position: absolute; top: 252px; left: 25px;
    display: flex; gap: 30px;
  }
  .page {
    position: relative; width: 560px; height: 396px;
    overflow: hidden; background: var(--paper);
    box-shadow: 0 6px 18px rgba(0,0,0,.18);
  }

  /* Back page */
  .back-photo {
    position: absolute; inset: 0;
    clip-path: polygon(56% 0, 100% 0, 100% 100%, 30% 100%);
    background:
      linear-gradient(180deg, rgba(255,255,255,0) 55%, rgba(120,80,50,.55) 100%),
      linear-gradient(100deg, #5d86b8 0%, #7fa4cf 40%, #c9d3dc 75%, #e7e2da 100%);
  }
  .back-veil {
    position: absolute; inset: 0;
    clip-path: polygon(84% 0, 100% 0, 100% 30%, 62% 100%, 48% 100%);
    background: rgba(255,255,255,.35);
  }
  .brand {
    display: flex; align-items: center; gap: 8px;
  }
  .brand-dot {
    width: 18px; height: 18px; border-radius: 50%;
    background: var(--sun-orange);
  }
  .brand-name {
    font-weight: 600; font-size: 13px; letter-spacing: .06em;
    color: var(--brand-blue); text-transform: uppercase;
  }
  .back-brand { position: absolute; top: 36px; left: 40px; }
  .details {
    position: absolute; top: 80px; left: 40px; width: 150px;
    color: var(--mid-blue); font-size: 9.5px; line-height: 1.3; font-weight: 400;
  }
  .details p { margin-bottom: 8px; }
  .details .label { display: block; }

  /* Cover */
  .cover-photo {
    position: absolute; inset: 0;
    background:
      linear-gradient(180deg, transparent 78%, #5a4a5c 84%, #8a7891 100%),
      linear-gradient(180deg, #a9b8d8 0%, #c4c3e0 35%, #e4c6d6 60%, #f0c9c0 76%);
  }
  .cover-square {
    position: absolute; left: 11%; top: 13%; width: 18%; height: 45%;
    background: rgba(52,160,224,.82);
  }
  .cover-band {
    position: absolute; inset: 0;
    clip-path: polygon(86% 0, 100% 0, 100% 100%, 92% 100%, 84% 40%);
    background: linear-gradient(180deg, rgba(255,255,255,.3) 0%, rgba(255,194,20,.45) 70%, rgba(247,143,32,.55) 100%);
  }
  .cover-brand {
    position: absolute; top: 24%; left: 34%; right: 16%;
    display: flex; flex-direction: column; align-items: center; gap: 10px;
  }
  .cover-brand .brand-dot {
    width: 34px; height: 34px; background: var(--white);
  }
  .cover-brand .brand-name {
    color: var(--white); font-size: 18px; font-weight: 400; letter-spacing: .08em;
    white-space: nowrap;
  }
</style>
</head>
<body>
  <main class="spread">
    <section class="page back-page">
      <div class="back-photo" role="img" aria-label="Photo of students in jeans standing in a bright café classroom"></div>
      <div class="back-veil"></div>
      <div class="brand back-brand">
        <span class="brand-dot"></span>
        <span class="brand-name">Tessaly Crane Int'l</span>
      </div>
      <div class="details">
        <p><span class="label">INFO:</span>Wednesday<br>Weekend<br>Classroom</p>
        <p><span class="label">Included:</span>housing, food, travel expenses, admission costs, visa form, insurance, books and stuff</p>
        <p><span class="label">Not included:</span>spending money, plane ticket</p>
        <p><span class="label">Contact info:</span>Jiwon Lee<br>010-5521-0387</p>
        <p>Email: hi@tessalycrane.example</p>
      </div>
    </section>

    <section class="page cover-page">
      <div class="cover-photo" role="img" aria-label="Photo of the Capitol in Washington D.C. at sunset with autumn trees and reflecting pool"></div>
      <div class="cover-square"></div>
      <div class="cover-band"></div>
      <div class="cover-brand">
        <span class="brand-dot"></span>
        <span class="brand-name">Tessaly Crane Int'l</span>
      </div>
    </section>
  </main>
</body>
</html>
```